Financial PR company Homepage and Inner Page design

Please design a web homepage and innerpage for LORVIA Public Relations.
LORVIA Public Relations is a Financial PR company targeting Shenzhen Qian Special Economical Zone.
Note:
1. Menu includes ( Please specialize in Chinese and we want to see the Chinese fonts)
关于我们/服务板块/专业优势/合作伙伴/前海商圈/公司新闻/加盟我们/联系我们

2. Please refer to world class PR Business company and contribute your idea on website design and color themes.

3. We have attached the Logo for reference.

4. Anytime use picture for reference, please select asian business people pictures.

Cheers,

HI Designers, Thanks for the design submission. Here is our client feedback: 1. Adopt one screen design. 2. Use amiable Asia Business woman pictures. 3. Use contrastive color theme for the design. Cheers, Kit From PW

```html
<!DOCTYPE html>
<html lang="en">
<head>
<meta charset="utf-8">
<title>LORVIA Public Relations</title>
<link href="https://fonts.googleapis.com/css2?family=Open+Sans:wght@400;600;700;800&display=swap" rel="stylesheet">
<style>
:root{
  --blue:#3aa8dc;
  --blue-dark:#1f86bd;
  --navy:#1b3a57;
  --navy-deep:#14304a;
  --ink:#2d3a45;
  --text:#5f6b75;
  --light:#eef0f2;
  --sky:#dff1fa;
  --footer:#2a2d31;
  --footer-bar:#3aa8dc;
  --white:#ffffff;
}
*{box-sizing:border-box;margin:0;padding:0}
html,body{width:1200px;height:2767px;overflow:hidden}
body{font-family:"Open Sans",Arial,sans-serif;color:var(--text);background:var(--white);font-size:14px;line-height:1.55}
.wrap{width:944px;margin:0 auto;position:relative}
a{color:inherit;text-decoration:none}

/* header */
.top-header{height:97px}
.top-header .wrap{display:flex;align-items:center;justify-content:space-between;height:97px}
.brand{display:flex;align-items:center;gap:12px}
.brand-mark{width:34px;height:34px;border-radius:50%;background:var(--blue)}
.brand-name{font-size:32px;font-weight:600;color:var(--blue);letter-spacing:1px}
.contact-pills{display:flex;gap:14px;margin-top:22px}
.pill{display:flex;align-items:center;gap:8px;border:1px solid #cfd6dc;border-radius:4px;padding:5px 12px;font-size:15px;color:var(--ink);font-weight:600}
.pill svg{width:18px;height:18px}

/* nav */
.main-nav{height:52px;background:var(--blue);border-top:3px solid var(--blue-dark)}
.main-nav ul{list-style:none;display:flex;height:49px;align-items:stretch}
.main-nav li{display:flex;align-items:center;padding:0 17px;color:var(--white);font-size:13px;font-weight:700;border-right:1px solid rgba(255,255,255,.25)}
.main-nav li.home{background:var(--navy);padding:0 13px}

/* hero */
.hero{height:467px;position:relative;background:linear-gradient(100deg,#e6eef3 0%,#c9d8e2 38%,#8fa6b8 70%,#5f7788 100%)}
.hero-copy{position:absolute;left:128px;top:78px;width:420px}
.hero-title{font-size:44px;font-weight:700;color:var(--navy);line-height:1.1}
.hero-sub{font-size:25px;font-weight:600;color:var(--navy);line-height:1.3;margin-top:14px}
.hero-text{font-size:13px;color:var(--ink);margin-top:16px;width:330px}
.btn{display:inline-block;background:var(--blue);color:var(--white);font-weight:700;font-size:13px;padding:8px 22px;border-radius:16px;margin-top:22px}

/* welcome */
.welcome{height:300px;text-align:center;padding-top:42px}
.section-title{font-size:32px;font-weight:600;color:var(--ink);letter-spacing:.5px}
.section-title span{color:var(--blue)}
.title-rule{width:70px;height:2px;background:var(--blue);margin:8px auto 16px}
.welcome p{font-size:13px;width:944px;margin:0 auto}
.btn-square{display:inline-block;background:var(--navy);color:var(--white);font-size:13px;font-weight:600;padding:7px 22px;border-radius:3px;margin-top:16px}

/* services */
.services{height:360px;background:linear-gradient(135deg,var(--navy) 0%,var(--navy-deep) 100%);text-align:center;padding-top:36px}
.services .section-title{color:var(--white)}
.services .lead{color:#c8d6e2;font-size:14px}
.service-list{display:flex;justify-content:space-between;width:800px;margin:34px auto 0}
.service{width:140px;color:var(--white);font-size:12px;font-weight:700;line-height:1.35}
.service-icon{width:100px;height:100px;border-radius:50%;border:4px solid var(--white);background:var(--white);margin:0 auto 12px;display:flex;align-items:center;justify-content:center}
.service-icon svg{width:52px;height:52px}

/* advantage */
.advantage{height:453px;background:var(--light);padding-top:41px}
.advantage-card{background:var(--white);height:362px;padding:28px 32px;display:flex;gap:34px;box-shadow:0 1px 3px rgba(0,0,0,.08)}
.advantage-card .section-title{text-align:left;font-size:28px}
.adv-copy{width:480px}
.adv-heading{font-size:16px;color:var(--blue);font-weight:600;margin-top:18px}
.adv-copy p{font-size:12px;margin-top:4px}
.ticks{list-style:none;margin-top:12px}
.ticks li{display:flex;gap:8px;align-items:center;font-size:12px;padding:4px 0;border-bottom:1px dotted #d5dbe0}
.ticks svg{width:13px;height:13px;flex:none}
.adv-visual{flex:1;margin-top:34px;height:268px;background:linear-gradient(135deg,#7fb6e0,#2f6eb3)}

/* join */
.join{height:235px;display:flex}
.join-photo{width:415px;background:linear-gradient(120deg,#dfe6ec,#9aaab8 55%,#4d6478)}
.join-body{flex:1;background:var(--sky);padding:26px 0 0 32px}
.join-body .section-title{font-size:30px;text-align:left}
.join-body p{font-size:12px;width:680px;margin-top:6px}
.btn-join{display:inline-flex;align-items:center;gap:8px;background:var(--navy);color:var(--white);font-size:13px;font-weight:600;padding:7px 16px;border-radius:3px;margin-top:14px}

/* partners */
.partners{height:104px;border-bottom:1px solid #e2e6e9}
.partners .wrap{display:flex;align-items:center;justify-content:space-between;height:104px}
.partner{font-size:24px;font-weight:700;color:#2a2a2a}
.arrow{width:20px;height:20px}

/* news */
.news{height:398px;text-align:center;padding-top:30px}
.news-grid{display:flex;justify-content:space-between;margin-top:6px;text-align:left}
.news-card{width:456px;display:flex;gap:18px}
.news-photo{width:210px;height:250px;background:linear-gradient(160deg,#d8dde2,#8796a4)}
.news-body h3{font-size:15px;color:var(--blue);font-weight:600}
.news-date{display:flex;align-items:center;gap:6px;font-size:12px;color:var(--ink);margin:8px 0}
.news-body p{font-size:12px}
.read-more{font-size:12px;color:var(--ink);font-weight:700;margin-top:6px;display:block}

/* footer */
.site-footer{height:259px;background:var(--footer);color:#b9c0c6;padding-top:28px}
.site-footer .wrap{display:flex}
.foot-col h4{color:var(--white);font-size:13px;font-weight:700;margin-bottom:12px}
.foot-links{width:198px;list-style:none}
.foot-links li{font-size:12px;padding:2px 0}
.foot-links li::before{content:"› ";color:var(--blue)}
.foot-news{width:285px;font-size:12px}
.foot-news .field{background:var(--white);height:28px;width:210px;margin-top:12px;color:#888;padding:5px 8px}
.foot-news .sub{display:inline-block;background:var(--blue);color:var(--white);font-weight:700;padding:5px 14px;margin-top:8px}
.foot-contact{width:220px;font-size:12px}
.foot-contact .row{display:flex;gap:8px;align-items:flex-start;margin-bottom:8px}
.foot-contact svg{width:14px;height:14px;flex:none;margin-top:2px}
.foot-map{width:241px;height:140px;margin-top:30px;background:linear-gradient(135deg,#e8ecd9,#c6d9e8)}
.bottom-bar{height:35px;background:var(--footer-bar);color:var(--white);font-size:12px}
.bottom-bar .wrap{display:flex;justify-content:space-between;align-items:center;height:35px}
.follow{display:flex;align-items:center;gap:8px}
.follow i{display:block;width:16px;height:16px;border-radius:50%;background:var(--white);opacity:.85}
</style>
</head>
<body>

<header class="top-header">
  <div class="wrap">
    <div class="brand"><span class="brand-mark"></span><span class="brand-name">LORVIA PR</span></div>
    <div class="contact-pills">
      <span class="pill"><svg viewBox="0 0 24 24"><path fill="#3aa8dc" d="M6.6 10.8a15.1 15.1 0 0 0 6.6 6.6l2.2-2.2c.3-.3.7-.4 1-.2 1.1.4 2.3.6 3.6.6.6 0 1 .4 1 1V20c0 .6-.4 1-1 1A17 17 0 0 1 3 4c0-.6.4-1 1-1h3.5c.6 0 1 .4 1 1 0 1.3.2 2.5.6 3.6.1.3 0 .7-.2 1z"/></svg>555-0142-880</span>
      <span class="pill"><svg viewBox="0 0 24 24"><rect x="2" y="5" width="20" height="14" rx="2" fill="#3aa8dc"/><path d="M3 6l9 7 9-7" stroke="#fff" stroke-width="2" fill="none"/></svg>info@lorviapr.com</span>
    </div>
  </div>
</header>

<nav class="main-nav">
  <div class="wrap">
    <ul>
      <li class="home"><svg width="20" height="20" viewBox="0 0 24 24"><path fill="#fff" d="M12 3l10 9h-3v9h-5v-6h-4v6H5v-9H2z"/></svg></li>
      <li>ABOUT US</li><li>SERVICE SECTOR</li><li>PROFESSIONAL ADVANTAGE</li><li>QIANHAI DISTRICT</li><li>COMPANY NEWS</li><li>JOIN US</li><li>CONTACT US</li>
    </ul>
  </div>
</nav>

<section class="hero" role="img" aria-label="Photo of four smiling Asian business people reviewing papers in a bright office">
  <div class="hero-copy">
    <h1 class="hero-title">OUR COMPANY IS A</h1>
    <p class="hero-sub">FINANCIAL PUBLIC RELATION COMPANY</p>
    <p class="hero-text">Autem vel eum iriure dolor in hendrerit in vulputate velit esse molestie consequat, vel illum dolore eu feugiat nulla facilisis.</p>
    <a class="btn">LEARN MORE ›</a>
  </div>
</section>

<section class="welcome">
  <h2 class="section-title">WELCOME TO <span>LORVIA PR</span></h2>
  <div class="title-rule"></div>
  <p>Lorem ipsum dolor sit amet, consectetuer adipiscing elit, sed diam nonummy nibh euismod tincidunt ut laoreet dolore magna aliquam erat volutpat. Ut wisi enim ad minim veniam, quis nostrud exerci tation ullamcorper suscipit lobortis nisl ut aliquip ex ea commodo consequat. Duis autem vel eum iriure dolor in hendrerit in vulputate velit esse molestie consequat, vel illum dolore eu feugiat nulla facilisis at vero eros et accumsan et iusto odio dignissim qui blandit praesent luptatum zzril delenit augue duis dolore te feugait nulla facilisi.</p>
  <a class="btn-square">Read More</a>
</section>

<section class="services">
  <h2 class="section-title">SERVICE <span>SECTOR</span></h2>
  <div class="title-rule"></div>
  <p class="lead">Ut wisi enim ad minim veniam, quis nostrud exerci tation ullamcorper suscipit lobortis ut aliquip.</p>
  <div class="service-list">
    <div class="service"><div class="service-icon"><svg viewBox="0 0 24 24"><path fill="#1b3a57" d="M12 2l10 5v2H2V7zM4 10h3v8H4zm6.5 0h3v8h-3zM17 10h3v8h-3zM2 19h20v3H2z"/></svg></div>MEDIA &amp; PUBLIC<br>RELATIONS</div>
    <div class="service"><div class="service-icon"><svg viewBox="0 0 24 24"><circle cx="8" cy="8" r="3.5" fill="#1b3a57"/><circle cx="16.5" cy="8.5" r="3" fill="#1b3a57"/><path fill="#1b3a57" d="M1 20c0-4 3-6.5 7-6.5s7 2.5 7 6.5zM15.5 13.5c4 0 7.5 2 7.5 6.5h-6.5c0-2.8-.5-4.8-1-6.5z"/></svg></div>GOVERNMENT<br>RELATIONS</div>
    <div class="service"><div class="service-icon"><svg viewBox="0 0 24 24"><circle cx="10" cy="10" r="6.5" stroke="#1b3a57" stroke-width="2.5" fill="none"/><path d="M15 15l6.5 6.5" stroke="#1b3a57" stroke-width="3" stroke-linecap="round"/></svg></div>PUBLIC RELATIONS<br>RESEARCH</div>
    <div class="service"><div class="service-icon"><svg viewBox="0 0 24 24"><rect x="2" y="4" width="20" height="13" rx="1.5" stroke="#1b3a57" stroke-width="2.2" fill="none"/><path fill="#1b3a57" d="M8 20h8v2H8zM10 8l6 2.5-6 2.5z"/></svg></div>ADVOCACY<br>ADVERTISING</div>
    <div class="service"><div class="service-icon"><svg viewBox="0 0 24 24"><circle cx="12" cy="12" r="9.5" stroke="#1b3a57" stroke-width="2" fill="none"/><circle cx="12" cy="12" r="5.5" stroke="#1b3a57" stroke-width="2" fill="none"/><circle cx="12" cy="12" r="2" fill="#1b3a57"/></svg></div>PR &amp; MARKETING<br>STRATEGIES</div>
  </div>
</section>

<section class="advantage">
  <div class="wrap advantage-card">
    <div class="adv-copy">
      <h2 class="section-title">PROFESSIONAL <span>ADVANTAGE</span></h2>
      <h3 class="adv-heading">Accumsan Et Iusto Odio Dignissim Qui Blandit Praesent</h3>
      <p>Lorem ipsum dolor sit amet, consectetuer adipiscing elit, sed diam nonummy nibh euismod tincidunt ut laoreet dolore magna aliquam erat volutpat. Ut wisi enim ad minim veniam, exerci tation.</p>
      <ul class="ticks">
        <li><svg viewBox="0 0 24 24"><path d="M3 12l6 6L21 5" stroke="#3aa8dc" stroke-width="3" fill="none"/></svg>Ut wisi enim ad minim veniam, quis nostrud exerci tation ullamcorper</li>
        <li><svg viewBox="0 0 24 24"><path d="M3 12l6 6L21 5" stroke="#3aa8dc" stroke-width="3" fill="none"/></svg>Duis autem vel eum iriure dolor in hendrerit in vulputate velit esse molestie</li>
        <li><svg viewBox="0 0 24 24"><path d="M3 12l6 6L21 5" stroke="#3aa8dc" stroke-width="3" fill="none"/></svg>Ut wisi enim ad minim veniam, quis nostrud exerci tation ullamcorper</li>
        <li><svg viewBox="0 0 24 24"><path d="M3 12l6 6L21 5" stroke="#3aa8dc" stroke-width="3" fill="none"/></svg>Vel illum dolore eu feugiat nulla facilisis at vero eros et accumsan et iusto odio</li>
      </ul>
    </div>
    <div class="adv-visual" role="img" aria-label="Illustration of blue jigsaw puzzle pieces with a public relations theme"></div>
  </div>
</section>

<section class="join">
  <div class="join-photo" role="img" aria-label="Photo of Asian business people shaking hands in an office"></div>
  <div class="join-body">
    <h2 class="section-title">JOIN <span>US</span></h2>
    <p>Lorem ipsum dolor sit amet, consectetuer adipiscing elit, sed diam nonummy nibh euismod tincidunt ut laoreet dolore magna aliquam erat volutpat. Ut wisi enim ad minim veniam, quis nostrud exerci tation ullamcorper suscipit lobortis nisl ut aliquip ex ea commodo consequat. Duis autem vel eum iriure dolor in hendrerit in vulputate velit esse molestie consequat, vel illum dolore eu feugiat nulla facilisis at vero eros et accumsan et iusto odio.</p>
    <a class="btn-join"><svg width="16" height="16" viewBox="0 0 24 24"><circle cx="12" cy="8" r="4" fill="#fff"/><path fill="#fff" d="M4 21c0-4.5 3.5-7 8-7s8 2.5 8 7z"/></svg>Join Us Now</a>
  </div>
</section>

<section class="partners">
  <div class="wrap">
    <svg class="arrow" viewBox="0 0 24 24"><path d="M15 4l-8 8 8 8" stroke="#888" stroke-width="2.5" fill="none"/></svg>
    <span class="partner">Northvale</span>
    <span class="partner">Corvane</span>
    <span class="partner">Tallgrove</span>
    <span class="partner">Brightmere</span>
    <span class="partner">Solvant</span>
    <svg class="arrow" viewBox="0 0 24 24"><path d="M9 4l8 8-8 8" stroke="#888" stroke-width="2.5" fill="none"/></svg>
  </div>
</section>

<section class="news">
  <h2 class="section-title">COMPANY <span>NEWS</span></h2>
  <div class="title-rule"></div>
  <div class="wrap news-grid">
    <article class="news-card">
      <div class="news-photo" role="img" aria-label="Photo of a smiling Asian businesswoman"></div>
      <div class="news-body">
        <h3>Lorem ipsum dolor sit a</h3>
        <div class="news-date"><svg width="14" height="14" viewBox="0 0 24 24"><rect x="3" y="5" width="18" height="16" rx="2" stroke="#3aa8dc" stroke-width="2" fill="none"/><path d="M3 10h18M8 3v4M16 3v4" stroke="#3aa8dc" stroke-width="2"/></svg>Oct 07, 2014</div>
        <p>Sed diam nonummy nibh euismod tincidunt ut laoreet dolore magna aliquam erat volutpat. Ut wisi enim ad minim veniam, quis nostrud exerci tation ullamcorper suscipit lobortis nisl ut aliquip ex ea commodo consequat.</p>
        <a class="read-more">Read More ›</a>
      </div>
    </article>
    <article class="news-card">
      <div class="news-photo" role="img" aria-label="Photo of a smiling Asian businessman in a suit"></div>
      <div class="news-body">
        <h3>Lorem ipsum dolor sit a</h3>
        <div class="news-date"><svg width="14" height="14" viewBox="0 0 24 24"><rect x="3" y="5" width="18" height="16" rx="2" stroke="#3aa8dc" stroke-width="2" fill="none"/><path d="M3 10h18M8 3v4M16 3v4" stroke="#3aa8dc" stroke-width="2"/></svg>Oct 07, 2014</div>
        <p>Sed diam nonummy nibh euismod tincidunt ut laoreet dolore magna aliquam erat volutpat. Ut wisi enim ad minim veniam, quis nostrud exerci tation ullamcorper suscipit lobortis nisl ut aliquip ex ea commodo consequat.</p>
        <a class="read-more">Read More ›</a>
      </div>
    </article>
  </div>
</section>

<footer class="site-footer">
  <div class="wrap">
    <div class="foot-col">
      <h4>QUICK LINKS</h4>
      <ul class="foot-links">
        <li>About Us</li><li>Service Sector</li><li>Professional Advantage</li><li>Qianhai District</li><li>Company News</li><li>Join Us</li>
      </ul>
    </div>
    <div class="foot-col foot-news">
      <h4>NEWSLETTER SIGNUP</h4>
      <p>Lorem ipsum dolor sit amet, consectetuer adipiscing elit, sed diam nonummy nibh euismod.</p>
      <div class="field">Email Address</div>
      <a class="sub">SUBSCRIBE</a>
    </div>
    <div class="foot-col foot-contact">
      <h4>CONTACT DETAIL</h4>
      <div class="row"><svg viewBox="0 0 24 24"><path fill="#3aa8dc" d="M12 2a7 7 0 0 0-7 7c0 5 7 13 7 13s7-8 7-13a7 7 0 0 0-7-7zm0 9.5A2.5 2.5 0 1 1 12 6.5a2.5 2.5 0 0 1 0 5z"/></svg><span>Unit 8 Harbourline Court,<br>Quayside Row,<br>Fenwick House, 5120</span></div>
      <div class="row"><svg viewBox="0 0 24 24"><path fill="#3aa8dc" d="M6.6 10.8a15.1 15.1 0 0 0 6.6 6.6l2.2-2.2c.3-.3.7-.4 1-.2 1.1.4 2.3.6 3.6.6.6 0 1 .4 1 1V20c0 .6-.4 1-1 1A17 17 0 0 1 3 4c0-.6.4-1 1-1h3.5c.6 0 1 .4 1 1 0 1.3.2 2.5.6 3.6.1.3 0 .7-.2 1z"/></svg><span>555-0142-880</span></div>
      <div class="row"><svg viewBox="0 0 24 24"><path fill="#3aa8dc" d="M6.6 10.8a15.1 15.1 0 0 0 6.6 6.6l2.2-2.2c.3-.3.7-.4 1-.2 1.1.4 2.3.6 3.6.6.6 0 1 .4 1 1V20c0 .6-.4 1-1 1A17 17 0 0 1 3 4c0-.6.4-1 1-1h3.5c.6 0 1 .4 1 1 0 1.3.2 2.5.6 3.6.1.3 0 .7-.2 1z"/></svg><span>555-0142-881</span></div>
      <div class="row"><svg viewBox="0 0 24 24"><rect x="2" y="5" width="20" height="14" rx="2" fill="#3aa8dc"/><path d="M3 6l9 7 9-7" stroke="#2a2d31" stroke-width="2" fill="none"/></svg><span>info@lorviapr.com</span></div>
    </div>
    <div class="foot-map" role="img" aria-label="Street map showing the office location"></div>
  </div>
</footer>

<div class="bottom-bar">
  <div class="wrap">
    <span>Copyright © 2014 Lorvia PR</span>
    <span class="follow">Follow Us: <i></i><i></i><i></i><i></i></span>
  </div>
</div>

</body>
</html>
```